Bookkeeping business needs a digital and print flyer

We need a flyer to promote our virtual bookkeeping services to small and mid-sized businesses in the United States. We want the content and design of the flyer to be consistent with our website: www.brightledgerbookkeeping.example. We would like both a print version and a digital version of the flyer.

```html
<!DOCTYPE html>
<html lang="en">
<head>
<meta charset="utf-8">
<title>Bright Ledger Bookkeeping – Flyer</title>
<link href="https://fonts.googleapis.com/css2?family=Montserrat:ital,wght@0,300;0,400;0,500;0,600;0,700;0,800;1,500;1,700&display=swap" rel="stylesheet">
<style>
  :root{
    --backdrop:#5f5f5f;
    --ink:#111111;
    --black:#0b0b0b;
    --paper:#ffffff;
    --gold:#fbbd2c;
    --gold-deep:#f2a81a;
    --gold-pale:#fde4a0;
    --white:#ffffff;
  }
  *{margin:0;padding:0;box-sizing:border-box}
  html,body{width:753px;height:1200px;overflow:hidden;background:var(--backdrop)}
  body{position:relative;font-family:"Montserrat",Arial,sans-serif;color:var(--ink)}
  .flyer{
    position:absolute;left:26.5px;top:109px;width:640px;height:898px;
    transform:scale(1.09375);transform-origin:0 0;
    background:var(--paper);overflow:hidden;
    box-shadow:0 6px 14px rgba(0,0,0,.45);
  }
  .hero{position:absolute;left:0;top:0;width:640px;height:440px;background:var(--black)}
  .hero-photo{
    position:absolute;left:0;top:0;width:640px;height:440px;
    background:
      linear-gradient(180deg,rgba(0,0,0,0) 0%,rgba(0,0,0,0) 55%,rgba(0,0,0,.75) 75%,#000 88%),
      linear-gradient(100deg,#6f8a4a 0%,#8c8f70 14%,#d9d2c6 24%,#8d8f95 38%,#c9c9cc 52%,#b8aaa0 70%,#e4dccf 82%,#efe8dc 100%);
  }
  .hero-shapes{position:absolute;left:0;top:0}
  .brand{position:absolute;left:32px;top:26px;display:flex;align-items:center;gap:12px;color:var(--white)}
  .brand-name{font-weight:300;font-size:25px;letter-spacing:1px;line-height:1}
  .brand-name small{display:block;font-size:12px;letter-spacing:1.5px;margin-top:3px;text-align:right}
  .brand-mark{width:44px;height:44px;border:2px solid var(--white);border-radius:50%}
  .headline{position:absolute;left:33px;top:222px;color:var(--gold);font-weight:800;font-size:38px;line-height:37px;text-shadow:0 2px 4px rgba(0,0,0,.6)}
  .tagline{position:absolute;left:33px;top:305px;color:var(--white);font-weight:700;font-size:17.5px}
  .services-label{position:absolute;left:33px;top:383px;color:var(--white);font-weight:700;font-size:15px}
  .services-hello{position:absolute;left:33px;top:406px;color:var(--gold);font-weight:700;font-size:18.5px}
  .section-title{position:absolute;font-weight:500;font-size:21px;line-height:23px}
  .section-title.left{left:32px;top:451px}
  .section-title.right{left:365px;top:451px}
  .list-label{position:absolute;left:33px;top:528px;font-weight:500;font-size:15.5px}
  .services-box{
    position:absolute;left:33px;top:550px;width:297px;height:273px;
    background:var(--gold);padding:9px 4px 0 14px;
  }
  .service-list{list-style:none}
  .service-list li{
    position:relative;padding-left:18px;font-weight:700;font-size:10.8px;line-height:12px;margin-bottom:9.5px;white-space:nowrap
  }
  .service-list li svg{position:absolute;left:0;top:1px}
  .benefit-list{position:absolute;left:368px;top:545px;width:260px;list-style:none}
  .benefit-list li{position:relative;padding-left:16px;font-size:11.6px;line-height:13.6px;font-weight:500}
  .benefit-list li svg{position:absolute;left:0;top:2px}
  .benefit-list em{font-weight:700}
  .footer-waves{position:absolute;left:0;top:812px}
  .contact{position:absolute;left:33px;top:869px;display:flex;align-items:center;gap:5px;font-weight:700;white-space:nowrap}
  .contact .phone{font-size:16px;margin-right:8px}
  .contact .small{font-size:8.8px}
  .contact svg{flex:none}
</style>
</head>
<body>
<main class="flyer">
  <section class="hero">
    <div class="hero-photo" role="img" aria-label="Photo of a wooden desk with a laptop, smartphone, pen, notebook and a green plant"></div>
    <svg class="hero-shapes" width="640" height="440" viewBox="0 0 640 440" aria-hidden="true">
      <path d="M0 0 H420 C370 14 330 50 300 80 C270 100 200 104 130 104 C80 104 30 100 0 98 Z" fill="#0b0b0b"/>
      <path d="M0 392 C110 370 220 395 330 388 C450 380 560 360 640 313 V440 H0 Z" fill="#0b0b0b"/>
      <path d="M0 378 C120 360 220 392 330 384 C450 375 560 352 640 310" fill="none" stroke="#fbbd2c" stroke-width="3"/>
    </svg>
    <div class="brand">
      <div class="brand-name">BRIGHT LEDGER<small>BOOKKEEPING</small></div>
      <div class="brand-mark"></div>
    </div>
    <h1 class="headline">Virtual Bookkeeping for<br>Small Business</h1>
    <p class="tagline">Build Your Business by Focusing on What You Love</p>
    <p class="services-label">Services</p>
    <p class="services-hello">Say Hello to a reliable, hassle-free bookkeeping solution!</p>
  </section>

  <h2 class="section-title left">Bookkeeping Tailored to<br>YOUR Business Needs</h2>
  <h2 class="section-title right">What you<br>get with Bright Ledger<br>Bookkeeping</h2>

  <p class="list-label">Services Available:</p>
  <svg style="position:absolute;left:0;top:0" width="640" height="898" aria-hidden="true">
    <path d="M190 540 H340 V826" fill="none" stroke="#f2a81a" stroke-width="2"/>
  </svg>

  <div class="services-box">
    <ul class="service-list">
      <li><svg width="11" height="11"><circle cx="5.5" cy="5.5" r="5.5" fill="#111"/><path d="M3 5.6 L4.9 7.4 L8 4" stroke="#fbbd2c" stroke-width="1.5" fill="none"/></svg>Catch-up and clean-up services</li>
      <li><svg width="11" height="11"><circle cx="5.5" cy="5.5" r="5.5" fill="#111"/><path d="M3 5.6 L4.9 7.4 L8 4" stroke="#fbbd2c" stroke-width="1.5" fill="none"/></svg>Transaction importation and categorization</li>
      <li><svg width="11" height="11"><circle cx="5.5" cy="5.5" r="5.5" fill="#111"/><path d="M3 5.6 L4.9 7.4 L8 4" stroke="#fbbd2c" stroke-width="1.5" fill="none"/></svg>Monthly reconciliation of all accounts,<br>including assets and loans.</li>
      <li><svg width="11" height="11"><circle cx="5.5" cy="5.5" r="5.5" fill="#111"/><path d="M3 5.6 L4.9 7.4 L8 4" stroke="#fbbd2c" stroke-width="1.5" fill="none"/></svg>Monthly financial reports (Balance Sheet,<br>Income Statement, Cash Flow)</li>
      <li><svg width="11" height="11"><circle cx="5.5" cy="5.5" r="5.5" fill="#111"/><path d="M3 5.6 L4.9 7.4 L8 4" stroke="#fbbd2c" stroke-width="1.5" fill="none"/></svg>Monthly video conference</li>
      <li><svg width="11" height="11"><circle cx="5.5" cy="5.5" r="5.5" fill="#111"/><path d="M3 5.6 L4.9 7.4 L8 4" stroke="#fbbd2c" stroke-width="1.5" fill="none"/></svg>Annual tax-prep package sent to<br>your preparer</li>
      <li><svg width="11" height="11"><circle cx="5.5" cy="5.5" r="5.5" fill="#111"/><path d="M3 5.6 L4.9 7.4 L8 4" stroke="#fbbd2c" stroke-width="1.5" fill="none"/></svg>&nbsp;A/R &amp; A/P</li>
      <li><svg width="11" height="11"><circle cx="5.5" cy="5.5" r="5.5" fill="#111"/><path d="M3 5.6 L4.9 7.4 L8 4" stroke="#fbbd2c" stroke-width="1.5" fill="none"/></svg>Payroll coordination</li>
      <li><svg width="11" height="11"><circle cx="5.5" cy="5.5" r="5.5" fill="#111"/><path d="M3 5.6 L4.9 7.4 L8 4" stroke="#fbbd2c" stroke-width="1.5" fill="none"/></svg>1099s</li>
      <li><svg width="11" height="11"><circle cx="5.5" cy="5.5" r="5.5" fill="#111"/><path d="M3 5.6 L4.9 7.4 L8 4" stroke="#fbbd2c" stroke-width="1.5" fill="none"/></svg>Bill pay and receipt management</li>
      <li><svg width="11" height="11"><circle cx="5.5" cy="5.5" r="5.5" fill="#111"/><path d="M3 5.6 L4.9 7.4 L8 4" stroke="#fbbd2c" stroke-width="1.5" fill="none"/></svg>Budgeting</li>
    </ul>
  </div>

  <ul class="benefit-list">
    <li style="margin-bottom:18px"><svg width="11" height="11"><rect x="0.6" y="1.6" width="8.5" height="8.5" fill="none" stroke="#111" stroke-width="1.1"/><path d="M2.5 5.5 L4.6 7.8 L10 1" stroke="#111" stroke-width="1.4" fill="none"/></svg>Worry no more about finding time and energy to tackle bookkeeping<br>&nbsp;– <em>Hakuna Matata!</em></li>
    <li style="margin-bottom:18px"><svg width="11" height="11"><rect x="0.6" y="1.6" width="8.5" height="8.5" fill="none" stroke="#111" stroke-width="1.1"/><path d="M2.5 5.5 L4.6 7.8 L10 1" stroke="#111" stroke-width="1.4" fill="none"/></svg>Keep more of your hard-earned money by maximizing tax deductions<br>&nbsp;– <em>Ka-Ching!</em></li>
    <li style="margin-bottom:18px"><svg width="11" height="11"><rect x="0.6" y="1.6" width="8.5" height="8.5" fill="none" stroke="#111" stroke-width="1.1"/><path d="M2.5 5.5 L4.6 7.8 L10 1" stroke="#111" stroke-width="1.4" fill="none"/></svg>Understand those confusing financial reports to take your business to the next level – <em>Booyah!</em></li>
    <li style="margin-bottom:16px"><svg width="11" height="11"><rect x="0.6" y="1.6" width="8.5" height="8.5" fill="none" stroke="#111" stroke-width="1.1"/><path d="M2.5 5.5 L4.6 7.8 L10 1" stroke="#111" stroke-width="1.4" fill="none"/></svg>Celebrate each month's wins during monthly consultations –<em>Hooray!</em></li>
    <li><svg width="11" height="11"><rect x="0.6" y="1.6" width="8.5" height="8.5" fill="none" stroke="#111" stroke-width="1.1"/><path d="M2.5 5.5 L4.6 7.8 L10 1" stroke="#111" stroke-width="1.4" fill="none"/></svg>Stress-free tax time – <em>Oh Yeah!</em></li>
  </ul>

  <svg class="footer-waves" width="640" height="86" viewBox="0 0 640 86" aria-hidden="true">
    <path d="M0 30 C60 10 110 40 180 30 C260 18 300 42 380 30 C470 16 540 30 640 6 V86 H0 Z" fill="#fde4a0"/>
    <path d="M0 40 C80 22 140 48 220 38 C300 28 360 44 440 34 C520 24 580 30 640 18 V86 H0 Z" fill="#fccf62"/>
    <path d="M0 50 C90 36 170 56 260 48 C350 40 440 54 520 44 C580 38 610 40 640 34 V86 H0 Z" fill="#fbbd2c"/>
  </svg>

  <div class="contact">
    <svg width="13" height="13" viewBox="0 0 13 13"><circle cx="6.5" cy="6.5" r="6.5" fill="#111"/><path d="M4 3.5 L5.3 3.3 L5.9 5 L5 5.7 C5.5 6.7 6.3 7.5 7.3 8 L8 7.1 L9.7 7.7 L9.5 9 C6.5 9.3 3.7 6.5 4 3.5Z" fill="#fbbd2c"/></svg>
    <span class="phone">555-014-2783</span>
    <svg width="11" height="11" viewBox="0 0 11 11"><circle cx="5.5" cy="5.5" r="4.9" fill="none" stroke="#111" stroke-width="1.1"/><rect x="3" y="3.8" width="5" height="3.6" fill="none" stroke="#111" stroke-width=".8"/><path d="M3 3.8 L5.5 5.8 L8 3.8" fill="none" stroke="#111" stroke-width=".8"/></svg>
    <span class="small">mara@brightledgerbookkeeping.example</span>
    <svg width="11" height="11" viewBox="0 0 11 11" style="margin-left:3px"><circle cx="5.5" cy="5.5" r="4.9" fill="none" stroke="#111" stroke-width="1.1"/><ellipse cx="5.5" cy="5.5" rx="2" ry="4.9" fill="none" stroke="#111" stroke-width=".8"/><path d="M0.6 5.5 H10.4" stroke="#111" stroke-width=".8"/></svg>
    <span class="small">www.brightledgerbookkeeping.example</span>
  </div>
</main>
</body>
</html>
```